Picture Ads

We need some banner ads for our home business opportunity, we are evolving from text to picture ads. I have added some examples of what other distributors are using. We are looking for something really eye catching with some good key words and nice bright colours and to include our photo (attached)
Key words to include:
Booming online business
Personal Development and Leadership Industry
Earn an executive income from home
Simple 3 step system
Make up to $5,000 per sale
Not MLM
The size needs to be: 1000 x 35 pixels
13.9 x 4.75 Inches
35.3 x 11.1 cm
I think different platforms accept different sizes, not too familiar with it yet, any guidance welcome. I've clicked project for 2 days if that is to prioritise the order?
Many thanks,
Maren

Industry/Entity Type

Business

```html
<!DOCTYPE html>
<html lang="en">
<head>
<meta charset="utf-8">
<title>Booming Online Business Banner</title>
<link href="https://fonts.googleapis.com/css2?family=Bebas+Neue&family=Arimo&family=Caveat:wght@500&display=swap" rel="stylesheet">
<style>
  :root {
    --red: #e0141c;
    --text-red: #d9151c;
    --white: #ffffff;
    --silver-light: #fbfbfb;
    --silver: #dcdcdc;
    --ink: #222222;
    --photo-dark: #3a2a24;
    --photo-mid: #7a5a46;
    --chart-red: #f3c9c4;
    --chart-amber: #f6e2c2;
    --chart-green: #d3e8c6;
  }
  * { margin: 0; padding: 0; box-sizing: border-box; }
  html, body { width: 1200px; height: 410px; overflow: hidden; background: var(--white); }
  .banner {
    position: relative;
    width: 1200px;
    height: 410px;
    overflow: hidden;
    background: linear-gradient(90deg, var(--silver) 0%, var(--silver-light) 35%, var(--silver-light) 55%, var(--silver) 75%);
  }
  .side-panel, .header-band { position: absolute; left: 0; top: 0; }
  .headline {
    position: absolute;
    left: 138px;
    top: 12px;
    font-family: "Bebas Neue", sans-serif;
    font-weight: 400;
    font-size: 76px;
    line-height: 76px;
    letter-spacing: 0.5px;
    color: var(--white);
    white-space: nowrap;
    text-shadow: 0 2px 2px rgba(0,0,0,0.25);
  }
  .cta {
    position: absolute;
    left: 908px;
    top: 32px;
    display: flex;
    align-items: center;
    gap: 34px;
    font-family: "Bebas Neue", sans-serif;
    font-size: 40px;
    line-height: 40px;
    letter-spacing: 2.5px;
    color: var(--white);
    text-decoration: none;
    white-space: nowrap;
  }
  .selling-points {
    position: absolute;
    right: 18px;
    top: 109px;
    list-style: none;
    text-align: right;
    font-family: "Arimo", Arial, sans-serif;
    font-size: 35px;
    line-height: 34px;
    color: var(--white);
  }
  .selling-points li {
    padding: 4px 4px 9px 0;
    margin-bottom: 8px;
    border-bottom: 4px dotted rgba(255,255,255,0.85);
    margin-left: auto;
    white-space: nowrap;
  }
  .selling-points li:nth-child(1) { width: 150px; }
  .selling-points li:nth-child(2) { width: 300px; white-space: normal; }
  .selling-points li:nth-child(3) { width: 340px; }
  .selling-points li:nth-child(4) { width: 424px; }
  .polaroid {
    position: absolute;
    left: 22px;
    top: 110px;
    width: 224px;
    height: 280px;
    background: var(--white);
    padding: 7px 7px 0;
    box-shadow: 2px 3px 8px rgba(0,0,0,0.35);
  }
  .portrait {
    width: 210px;
    height: 236px;
    background: radial-gradient(ellipse at 60% 50%, var(--photo-mid), var(--photo-dark));
  }
  .caption {
    font-family: "Caveat", cursive;
    font-size: 15px;
    line-height: 18px;
    color: var(--ink);
    text-align: center;
    margin-top: 10px;
  }
  .growth-visual {
    position: absolute;
    left: 306px;
    top: 100px;
    width: 318px;
    height: 200px;
    background: linear-gradient(90deg, var(--chart-red) 0%, var(--chart-amber) 55%, var(--chart-green) 100%);
    border-radius: 4px;
  }
  .industry {
    position: absolute;
    left: 266px;
    top: 306px;
    font-family: "Bebas Neue", sans-serif;
    font-weight: 400;
    font-size: 49px;
    line-height: 48px;
    letter-spacing: 1px;
    text-transform: uppercase;
    color: var(--text-red);
    white-space: nowrap;
  }
</style>
</head>
<body>
<div class="banner">
  <svg class="side-panel" width="1200" height="410" viewBox="0 0 1200 410">
    <defs>
      <linearGradient id="panelFill" x1="0" y1="0" x2="1" y2="1">
        <stop offset="0" stop-color="#f01a1e"/>
        <stop offset="1" stop-color="#c20b10"/>
      </linearGradient>
    </defs>
    <polygon points="880,0 1200,0 1200,410 738,410 858,84" fill="url(#panelFill)"/>
  </svg>

  <svg class="header-band" width="1200" height="84" viewBox="0 0 1200 84">
    <defs>
      <linearGradient id="bandFill" x1="0" y1="0" x2="0" y2="1">
        <stop offset="0" stop-color="#f24a22"/>
        <stop offset="0.5" stop-color="#e0141c"/>
        <stop offset="1" stop-color="#a8080d"/>
      </linearGradient>
      <linearGradient id="ctaFill" x1="0" y1="0" x2="0" y2="1">
        <stop offset="0" stop-color="#c8101a"/>
        <stop offset="1" stop-color="#8e0508"/>
      </linearGradient>
    </defs>
    <rect x="0" y="0" width="1200" height="84" fill="url(#bandFill)"/>
    <polygon points="880,0 1200,0 1200,84 858,84" fill="url(#ctaFill)"/>
  </svg>

  <h1 class="headline">Booming Online Business!</h1>
  <a class="cta" href="#">Get Started
    <svg width="26" height="22" viewBox="0 0 26 22"><path d="M0 8h14V1l12 10-12 10v-7H0z" fill="#ffffff"/></svg>
  </a>

  <ul class="selling-points">
    <li>Not MLM</li>
    <li>Earn an executive income from home</li>
    <li>Simple 3 step system</li>
    <li>Make up to $5000 per sale</li>
  </ul>

  <figure class="polaroid">
    <div class="portrait" role="img" aria-label="Portrait photo of Maren and Odette Halloway"></div>
    <figcaption class="caption">Maren and Odette Halloway</figcaption>
  </figure>

  <div class="growth-visual" role="img" aria-label="Illustration of a rising growth chart with an upward arrow"></div>

  <p class="industry">Personal Development<br>&amp; Leadership Industry</p>
</div>
</body>
</html>
```